Power point presentation optimization, in terms of content design

I have a completed business presentation, with all the texting, but I need some design improvement in terms of text formatting, lettering, text boxes, arrows, bullets, shapes and their formatting, relative location of text boxes and pictures in the slide, etc, etc, so that this specific presentation becomes more visually appealing.
Our company power point template is available.
I´m providing our company power point template (to be used as a reference) as well as the presentation that needs to be improved.

Target Market(s)

Potential partner in business.

Industry/Entity Type

Health

Requirements
Nice to have
• More ellegant collors (more according to the template) on the picture of slide 7. A more elegant dollar image (slide 16).

```html
<!DOCTYPE html>
<html lang="pt">
<head>
<meta charset="utf-8">
<title>Centro Clínico Atlântico — Apresentação</title>
<link href="https://fonts.googleapis.com/css2?family=Poppins:wght@400;500;600;700&display=swap" rel="stylesheet">
<style>
:root{
  --navy:#1b3a6b;
  --teal:#2e7ea6;
  --ink:#1d1d1f;
  --text:#333;
  --page:#eef0f2;
  --white:#fff;
}
*{margin:0;padding:0;box-sizing:border-box}
html,body{width:1200px;height:3652px;overflow:hidden;background:var(--page);font-family:'Poppins',sans-serif;color:var(--text)}
.slide{position:absolute;left:99px;width:1002px;height:563px;background:var(--white);overflow:hidden}
.abs{position:absolute}
.band{position:absolute;left:0;top:0}
.band-title{position:absolute;left:18px;top:14px;color:var(--white);font-weight:700;font-size:25px;letter-spacing:.5px;white-space:nowrap}
.brand{position:absolute;right:18px;top:18px;display:flex;align-items:center;gap:8px;color:var(--navy);font-weight:700;font-size:16px;white-space:nowrap}
.brand i{width:22px;height:22px;background:var(--navy);display:block}
.pnum{position:absolute;right:14px;bottom:20px;width:27px;height:27px;border-radius:50%;background:#111;color:#fff;font-size:12px;font-weight:600;display:flex;align-items:center;justify-content:center}
.box{position:absolute;background:var(--navy);color:#fff;border-radius:6px;font-size:20px;line-height:1.45;display:flex;align-items:center;padding:0 20px}
.box.teal{background:var(--teal)}
.heading{position:absolute;left:0;width:100%;text-align:center;color:var(--teal);font-weight:700;font-size:34px;letter-spacing:.5px}
.photo{position:absolute}
/* slide 1 */
.cover-name{position:absolute;left:36px;top:56px;width:310px;display:flex;align-items:center;gap:12px;color:var(--navy);font-weight:700;font-size:26px;line-height:1.05}
.cover-name i{flex:0 0 52px;width:52px;height:52px;background:var(--navy);display:block}
.cover-title{position:absolute;left:36px;top:210px;color:var(--ink);font-weight:700;font-size:41px;line-height:1.05}
.cover-sub{position:absolute;left:36px;top:325px;color:var(--navy);font-weight:700;font-size:24px;line-height:1.55}
/* slide 3 */
.checks{position:absolute;left:258px;top:398px;list-style:none;font-size:14px;line-height:28px;color:var(--text)}
.checks li{padding-left:40px;position:relative}
.checks li.tick::before{content:"";position:absolute;left:4px;top:8px;width:11px;height:6px;border-left:2px solid var(--ink);border-bottom:2px solid var(--ink);transform:rotate(-45deg)}
/* slide 5 */
.about{position:absolute;left:522px;top:128px;width:460px;font-size:13px;line-height:22.5px}
.about p+p{margin-top:14px}
.pill{position:absolute;background:var(--teal);color:#fff;border-radius:4px;font-size:20px;display:flex;align-items:center;justify-content:center}
/* slide 6 */
.bio{position:absolute;left:380px;top:95px;width:605px}
.bio h3{color:var(--navy);font-size:19px;font-weight:600;margin-bottom:2px}
.bio p{font-size:13px;line-height:22.5px}
.bio section+section{margin-top:16px}
</style>
</head>
<body>

<section class="slide" style="top:57px">
  <div class="cover-name"><i></i><span>Centro Clínico<br>Atlântico</span></div>
  <h1 class="cover-title">Centro de<br>Telemedicina</h1>
  <p class="cover-sub">Uma perspetiva de<br>5 minutos</p>
  <div class="photo" role="img" aria-label="Médica a segurar um tablet com imagens médicas" style="left:378px;top:0;width:624px;height:563px;background:linear-gradient(135deg,#e9ecee,#cfd6dc 60%,#b8c2cb)"></div>
</section>

<section class="slide" style="top:648px">
  <svg class="band" width="600" height="67"><polygon points="0,0 596,0 529,67 0,67" fill="var(--navy)"/></svg>
  <div class="band-title">IMAGIOLOGIA EM ANGOLA</div>
  <div class="brand"><i></i>Centro Clínico Atlântico</div>
  <div class="heading" style="top:98px">CONTEXTO DE OPORTUNIDADE</div>
  <svg class="abs" style="left:0;top:0" width="1002" height="563">
    <line x1="357" y1="150" x2="645" y2="150" stroke="var(--navy)" stroke-width="3"/>
    <line x1="501" y1="150" x2="501" y2="220" stroke="var(--navy)" stroke-width="3"/>
    <line x1="352" y1="322" x2="440" y2="322" stroke="var(--navy)" stroke-width="3"/>
    <line x1="562" y1="322" x2="650" y2="322" stroke="var(--navy)" stroke-width="3"/>
    <circle cx="501" cy="322" r="62" fill="var(--navy)"/>
    <line x1="501" y1="398" x2="501" y2="430" stroke="var(--navy)" stroke-width="4"/>
    <polygon points="492,426 510,426 501,440" fill="var(--navy)"/>
  </svg>
  <div class="box" style="left:47px;top:250px;width:305px;height:144px">Carência dramática de cuidados na área da Imagiologia</div>
  <div class="box" style="left:650px;top:250px;width:305px;height:144px">Carência dramática de cuidados na área da Imagiologia</div>
  <div class="box teal" style="left:292px;top:457px;width:416px;height:68px;justify-content:center;font-weight:600;font-size:20px">Oportunidade comercial relevante</div>
  <div class="pnum">2</div>
</section>

<section class="slide" style="top:1243px">
  <svg class="band" width="600" height="67"><polygon points="0,0 596,0 529,67 0,67" fill="var(--navy)"/></svg>
  <div class="band-title">IMAGIOLOGIA EM ANGOLA</div>
  <div class="brand"><i></i>Centro Clínico Atlântico</div>
  <div class="heading" style="top:98px">A DIFICULDADE</div>
  <svg class="abs" style="left:0;top:0" width="1002" height="563">
    <line x1="357" y1="150" x2="645" y2="150" stroke="var(--navy)" stroke-width="3"/>
    <line x1="376" y1="245" x2="440" y2="245" stroke="var(--navy)" stroke-width="3"/>
    <line x1="562" y1="245" x2="625" y2="245" stroke="var(--navy)" stroke-width="3"/>
    <circle cx="501" cy="245" r="62" fill="var(--navy)"/>
  </svg>
  <div class="box" style="left:71px;top:196px;width:305px;height:98px">Falta de Médicos Radiologistas</div>
  <div class="box" style="left:625px;top:196px;width:305px;height:98px">Falta de Médicos Radiologistas</div>
  <div class="abs" style="left:0;top:361px;width:100%;text-align:center;color:var(--navy);font-weight:600;font-size:19px">A HIPÓTESE</div>
  <div class="box teal" style="left:30px;top:382px;width:213px;height:141px;font-size:18px">Expatriar Profissionais Portugueses</div>
  <ul class="checks">
    <li class="tick">Serviço de qualidade Europeia: necessários pelo menos 7</li>
    <li>Médicos Radiologistas nas diferentes sub-especialidades</li>
    <li class="tick">Portugal e Brasil também com enorme falta de Médicos</li>
    <li class="tick">Custo elevado fixo</li>
  </ul>
  <div class="box teal" style="left:746px;top:382px;width:213px;height:141px;font-size:18px">Elevado custo</div>
  <div class="pnum">3</div>
</section>

<section class="slide" style="top:1837px">
  <svg class="band" width="600" height="67"><polygon points="0,0 596,0 529,67 0,67" fill="var(--navy)"/></svg>
  <div class="band-title">IMAGIOLOGIA EM ANGOLA</div>
  <div class="brand"><i></i>Centro Clínico Atlântico</div>
  <div class="photo" role="img" aria-label="Radiologista a analisar exames em vários monitores" style="left:0;top:67px;width:500px;height:496px;background:linear-gradient(120deg,#1c2a3a,#3d5d80 45%,#a9b3bb 75%,#6d6a64)"></div>
  <div class="abs" style="left:565px;top:235px;color:var(--teal);font-weight:700;font-size:42px;line-height:1.3">A SOLUÇÃO –<br>TELERADIOLOGIA</div>
  <div class="pnum">4</div>
</section>

<section class="slide" style="top:2438px">
  <svg class="band" width="600" height="67"><polygon points="0,0 596,0 529,67 0,67" fill="var(--navy)"/></svg>
  <div class="band-title">SOBRE NÓS</div>
  <div class="brand"><i></i>Centro Clínico Atlântico</div>
  <div class="photo" role="img" aria-label="Esquema de serviço de teleradiologia ligando hospital, servidores e radiologistas" style="left:28px;top:128px;width:397px;height:382px;background:radial-gradient(ellipse at 45% 45%,#c9d6ea,#eef2f7 70%,#fff)"></div>
  <div class="about">
    <p>O Centro Internacional de Telemedicina Centro Clínico Atlântico nasceu da necessidade de assegurar uma resposta de teleradiologia de elevada qualidade, suportada por um corpo clínico de topo.</p>
    <p>Os nossos médicos são sub-especializados nas diferentes áreas: sistema musculo-esquelético, medicina desportiva, neurorradiologia, abdómen, pélvis, sistema cardiovascular e mama.<br>Todos os nossos exames recebem assim uma consultadoria diferenciada por especialistas de renome, assegurando o máximo rigor diagnóstico.</p>
  </div>
  <div class="pill" style="left:522px;top:384px;width:265px;height:56px">Os melhores Médicos</div>
  <div class="pill" style="left:522px;top:450px;width:172px;height:55px">EM LUANDA</div>
  <div class="pill" style="left:704px;top:450px;width:171px;height:55px">Baixo custo</div>
  <div class="pnum">5</div>
</section>

<section class="slide" style="top:3035px">
  <svg class="band" width="600" height="67"><polygon points="0,0 596,0 529,67 0,67" fill="var(--navy)"/></svg>
  <div class="band-title">RUI TAVARES MENDES</div>
  <div class="brand"><i></i>Centro Clínico Atlântico</div>
  <div class="photo" role="img" aria-label="Retrato do médico de fato escuro" style="left:0;top:67px;width:360px;height:496px;background:linear-gradient(180deg,#1a1a1a,#2c2c2e 60%,#3a3a3c)"></div>
  <div class="bio">
    <section>
      <h3>Educação Universitária</h3>
      <p>Licenciado em Medicina pela Faculdade de Medicina da Universidade do Tejo (FMT), com a classificação final de 17,17 valores (2000). Doutorado em Medicina pela FMT, aprovado por Unanimidade com Distinção e Louvor (2012).</p>
    </section>
    <section>
      <h3>Educação Pós-Graduada</h3>
      <p>Médico Interno de Imagiologia e Radiodiagnóstico do Hospital Universitário da Estrela (2003 a 2008).<br>Visiting Clinical Fellow – Vascular Imaging, Pacific Coast University, San Marino (2008).<br>Visiting Clinical Fellow – Musculoskeletal Imaging, Service de Radiologie Ostéoarticulaire, Hôpital Saint-Lazare, Lyon (2008).</p>
    </section>
    <section>
      <h3>Funções Actuais</h3>
      <p>CEO, Centro Clínico Atlântico (desde 2013). Membro da Comissão Editorial do “Global Review of Orthopaedic Imaging” (ISSN 0000-0000) (desde 2014). Grau de Consultor (Imagiologia) pelo Conselho Nacional Médico (desde 2018). Professor Auxiliar Convidado e Regente de Disciplina da Escola Médica Atlântica - FCM (desde 2018). Investigador do Centro de Investigação em Saúde Integrada, CISI/EMA (desde 2018).</p>
    </section>
  </div>
  <div class="pnum">6</div>
</section>

</body>
</html>
```